Business cards for 3 Realtors at one brokerage

We will need a business card template that can be projected on 3 business cards. Harborline Homes & Capital Corp. has 3 realtors on staff Dale, Owen, and Marcus. We all want a business card that shows our new logo and information. I will attach many versions of our Logo as well as head shots for each realtor (Owen- Long hair, youngest. Marcus- Suit jacket, parted hair cut. Dale- Angled Pose, Shirt and Tie.) I have attached our information below.

Dale Pinsworth
801-555-0147
dale@harborlinehomesco.com
Principal Broker

Marcus Ferndale
801-555-0192
marcus@harborlinehomesco.com
Real Estate Agent

Owen Ferndale
801-555-0163
owen@harborlinehomesco.com
Real Estate Agent

Harborline Homes & Capital Corp.
HarborlineHomesCo.com
2918 E 8250 Suite 207-316, South Jordan, UT 84009

Please feel free to reach out with any questions, comments, or concerns.

```html
<!DOCTYPE html>
<html lang="en">
<head>
<meta charset="utf-8">
<title>Harborline Homes &amp; Capital Corp. — Business Cards</title>
<link rel="stylesheet" href="https://fonts.googleapis.com/css2?family=Montserrat:wght@500;600;700&family=Arimo:wght@400&display=swap">
<style>
  :root {
    --stage: #1d1d1d;
    --brand-blue: #38a8f4;
    --ink: #1f1f1f;
    --slate: #6b6b6b;
    --paper: #ffffff;
    --band-grey: #727272;
    --photo-warm: #9a5a22;
    --photo-deep: #6e3c14;
  }
  * { box-sizing: border-box; margin: 0; padding: 0; }
  html, body { width: 1200px; height: 1015px; overflow: hidden; }
  body {
    background: var(--stage);
    font-family: "Arimo", Arial, sans-serif;
    position: relative;
  }
  .card {
    position: absolute;
    left: 250px;
    width: 700px;
    height: 400px;
    overflow: hidden;
    box-shadow: 0 12px 30px rgba(0,0,0,.6);
  }
  /* Front */
  .card--front { top: 60px; background: var(--brand-blue); color: var(--paper); }
  .front-brand {
    position: absolute; left: 0; right: 0; top: 95px;
    display: flex; flex-direction: column; align-items: center; gap: 18px;
  }
  .brand-mark {
    width: 92px; height: 92px; border-radius: 50%;
    border: 7px solid currentColor;
  }
  .brand-name {
    font-family: "Montserrat", sans-serif; font-weight: 600;
    font-size: 30px; letter-spacing: 3px; text-transform: uppercase;
    text-align: center; line-height: 1.25;
  }
  .front-web {
    position: absolute; left: 40px; right: 40px; top: 300px;
    display: flex; align-items: center; gap: 14px;
    font-size: 16px; letter-spacing: .5px;
  }
  .front-web .rule { flex: 1; height: 1px; background: rgba(255,255,255,.75); }

  /* Back */
  .card--back { top: 520px; background: var(--paper); }
  .back-brand {
    position: absolute; left: 60px; top: 50px; width: 330px;
    display: flex; flex-direction: column; align-items: center; gap: 14px;
    color: var(--slate);
  }
  .back-brand .brand-mark { width: 72px; height: 72px; border-width: 5px; border-color: var(--brand-blue); }
  .back-brand .brand-name { font-size: 21px; letter-spacing: 2px; }
  .contact-list {
    position: absolute; left: 70px; top: 220px; list-style: none;
    color: var(--ink); font-size: 18px; line-height: 1.2;
  }
  .contact-list li { display: flex; align-items: flex-start; gap: 10px; margin-bottom: 12px; }
  .contact-list svg { flex: none; width: 22px; height: 22px; margin-top: 1px; }
  .contact-list .tight { margin-bottom: 4px; }

  .agent-photo-frame {
    position: absolute; left: 445px; top: 30px; width: 225px; height: 225px;
    border: 2px solid var(--brand-blue); padding: 6px;
  }
  .agent-photo {
    width: 100%; height: 100%;
    background: linear-gradient(160deg, var(--photo-warm), var(--photo-deep));
  }
  .agent-name {
    position: absolute; right: 30px; top: 268px; text-align: right;
  }
  .agent-name h1 {
    font-family: "Montserrat", sans-serif; font-weight: 700; font-size: 24px;
    color: var(--brand-blue); letter-spacing: .5px; text-transform: uppercase;
  }
  .agent-name p { font-size: 18px; color: var(--ink); margin-top: 2px; }
  .band-grey {
    position: absolute; left: 0; bottom: 0; width: 430px; height: 24px;
    background: var(--band-grey);
  }
  .band-blue {
    position: absolute; right: 0; bottom: 0; width: 290px; height: 60px;
    background: var(--brand-blue); color: var(--paper);
    display: flex; align-items: center; justify-content: center; font-size: 17px;
  }
</style>
</head>
<body>

<section class="card card--front" aria-label="Card front">
  <div class="front-brand">
    <span class="brand-mark" aria-hidden="true"></span>
    <div class="brand-name">Harborline Homes<br>&amp; Capital Corp.</div>
  </div>
  <div class="front-web">
    <span class="rule"></span>
    <span>www.HarborlineHomesCo.com</span>
    <span class="rule"></span>
  </div>
</section>

<section class="card card--back" aria-label="Card back">
  <div class="back-brand">
    <span class="brand-mark" aria-hidden="true"></span>
    <div class="brand-name">Harborline Homes<br>&amp; Capital Corp.</div>
  </div>

  <ul class="contact-list">
    <li>
      <svg viewBox="0 0 24 24" aria-hidden="true"><circle cx="12" cy="12" r="10.5" fill="none" stroke="#38a8f4" stroke-width="2"/><path d="M12 6.5a3.6 3.6 0 0 0-3.6 3.6c0 2.7 3.6 7 3.6 7s3.6-4.3 3.6-7A3.6 3.6 0 0 0 12 6.5z" fill="#38a8f4"/><circle cx="12" cy="10.1" r="1.3" fill="#fff"/></svg>
      <span>2918 E 8250 Suite 207-316<br>South Jordan, UT 84009</span>
    </li>
    <li class="tight">
      <svg viewBox="0 0 24 24" aria-hidden="true"><circle cx="12" cy="12" r="10.5" fill="none" stroke="#38a8f4" stroke-width="2"/><path d="M8.3 6.8l2 2.3-1.1 1.4a7 7 0 0 0 4.3 4.3l1.4-1.1 2.3 2-1.2 1.6c-4.6-.3-8.6-4.3-8.9-8.9z" fill="#38a8f4"/></svg>
      <span>801-555-0163</span>
    </li>
    <li>
      <svg viewBox="0 0 24 24" aria-hidden="true"><circle cx="12" cy="12" r="10.5" fill="none" stroke="#38a8f4" stroke-width="2"/><rect x="6.5" y="8" width="11" height="8" fill="#38a8f4"/><path d="M6.5 8l5.5 4.5L17.5 8" fill="none" stroke="#fff" stroke-width="1.2"/></svg>
      <span>owen@harborlinehomesco.com</span>
    </li>
  </ul>

  <div class="agent-photo-frame">
    <div class="agent-photo" role="img" aria-label="Headshot of Owen Ferndale in a white shirt against a warm wooden wall"></div>
  </div>

  <div class="agent-name">
    <h1>Owen Ferndale</h1>
    <p>Real Estate Agent</p>
  </div>

  <div class="band-grey" aria-hidden="true"></div>
  <div class="band-blue">www.HarborlineHomesCo.com</div>
</section>

</body>
</html>
```